Childrens Development/Fun Centre needs a Kid-Centric website

We need a website devoted to what we love, children, this site should be similar to other children development centre website which offer similar services and developments (best example - m a r r o w k i n . c o . u k)

We need to reflect our values of being fun and friendly whilst also imparting important skills and knowledge onto children. The website should have a button at the top for login (we are using the same MIS system as the example website listed above - so the login and members pages will be hosted by a third party site).

The site should incorporate a like us on facebook button, a instagram feed (please only use alpine phototile plugin for the instagram, for the twitter you can just use the standard code from twitter no need for a plugin)

We need to have mailpoet on the site too with a form to join our mailing list.

Initially we want to see some nice designs which are similar in feel and vibe of the logo which is enclosed, in a format the same as the example listed above.

thanks

Reason: Hi, Apologies for the delay and the miscommunication, we need this website actually CODED, the design can be directly based on the design of the website mentioned in the brief. please only submit or send me a message if your proposal was for CODING! thanks

```html
<!DOCTYPE html>
<html lang="en">
<head>
<meta charset="utf-8">
<title>PlayNest – Children's Development Centre</title>
<link href="https://fonts.googleapis.com/css2?family=Ubuntu:wght@400;500;700&family=Lato:ital,wght@0,400;0,700;1,400&family=Oswald:wght@400;500&display=swap" rel="stylesheet">
<style>
:root{
  --green:#8cc63f;
  --green-dark:#2e9e3e;
  --green-title:#25a046;
  --navy:#3b3b98;
  --navy-deep:#1f2d8c;
  --cyan:#3fd2ea;
  --grey-bg:#efefef;
  --text:#333;
  --footer:#21a24a;
}
*{box-sizing:border-box;margin:0;padding:0}
html,body{width:757px;height:1200px;overflow:hidden;background:#fff}
body{position:relative;font-family:'Lato',sans-serif;color:var(--text)}
.abs{position:absolute}

/* header */
.site-header{position:absolute;left:0;top:0;width:757px;height:130px;background:linear-gradient(#fff,#e9e9e9)}
.brand{position:absolute;left:88px;top:18px;display:flex;align-items:center;gap:8px;font-family:'Ubuntu',sans-serif;font-weight:700;font-size:40px;color:var(--green-dark);letter-spacing:-1px}
.brand-dot{width:14px;height:14px;border-radius:50%;background:var(--navy)}
.top-link{position:absolute;font-family:'Lato',sans-serif;font-size:8px;color:#fff;background:var(--navy);padding:1px 4px;border:1px solid #fff;box-shadow:0 0 0 1px var(--navy)}
.top-link::before{content:"";position:absolute;left:50%;bottom:100%;width:1px;background:var(--navy);height:var(--h)}
.main-nav{position:absolute;left:82px;top:84px;display:flex}
.tab{width:85px;height:46px;display:flex;align-items:flex-end;justify-content:center;padding-bottom:8px;font-family:'Ubuntu',sans-serif;font-weight:500;font-size:12px;color:#fff;background:var(--green);clip-path:polygon(0 6px,60% 0,100% 6px,100% 100%,0 100%);border-right:1px solid #a6d46a}
.tab.active{background:var(--navy)}

/* hero */
.hero{position:absolute;left:0;top:130px;width:757px;height:295px;background:linear-gradient(120deg,#e9e4dc 0%,#f2ede6 40%,#d9b89a 70%,#c99a6f 100%)}
.hero-caption{position:absolute;left:0;top:220px;width:370px;height:62px;background:rgba(140,198,63,.78);clip-path:polygon(0 0,94% 0,100% 100%,0 100%);font-family:'Oswald',sans-serif;font-size:19px;line-height:26px;color:#2b2b2b;padding:4px 0 0 89px}
.hero-caption b{font-weight:500}
.slider-corner{position:absolute;right:0;bottom:0}
.slider-dots{position:absolute;right:35px;bottom:9px;font-family:'Ubuntu',sans-serif;font-weight:700;font-size:12px;color:#fff;letter-spacing:2px}
.slider-dots span{color:var(--green)}

/* welcome */
.welcome-title{position:absolute;left:0;width:757px;top:446px;text-align:center;font-family:'Ubuntu',sans-serif;font-weight:700;font-size:21px;color:var(--green-title)}
.welcome-brand{position:absolute;left:0;width:757px;top:472px;text-align:center;font-family:'Ubuntu',sans-serif;font-weight:700;font-size:28px;color:var(--green-dark)}
.welcome-text{position:absolute;left:90px;width:577px;top:532px;text-align:center;font-size:8.6px;line-height:14.2px;color:#444}
.btn{position:absolute;font-family:'Ubuntu',sans-serif;font-weight:500;font-size:8.5px;color:#fff;text-align:center;border-radius:2px}
.btn-green{background:var(--green);border:1px solid #6fa52c}
.btn-navy{background:var(--navy)}

/* features */
.features{position:absolute;left:0;top:640px;width:757px;height:255px}
.card{position:absolute;top:54px;width:183px;height:172px;background:#fff;border:1px solid var(--green)}
.card h2{position:absolute;left:11px;top:10px;font-family:'Ubuntu',sans-serif;font-weight:500;font-size:14px;color:var(--green-title)}
.card .photo{position:absolute;left:12px;top:36px;width:158px;height:70px}
.card p{position:absolute;left:11px;top:114px;width:164px;font-size:8.3px;line-height:14px;color:#333}
.card .btn{left:59px;top:161px;width:65px;height:17px;line-height:17px}

/* social */
.section-title{position:absolute;top:918px;font-family:'Ubuntu',sans-serif;font-weight:500;font-size:14px;color:var(--green-title)}
.insta{position:absolute;width:80px;height:72px;outline:1px solid #e6e6e6;outline-offset:2px}
.feed{position:absolute;top:942px;width:136px;height:160px;padding:5px}
.feed.updates{left:379px;background:var(--cyan)}
.feed.community{left:532px;background:var(--navy-deep)}
.feed-head{height:18px;display:flex;align-items:center;justify-content:space-between;color:#fff;font-size:9px;padding:0 2px 4px}
.feed-head .dot{display:inline-block;width:9px;height:9px;border-radius:50%;background:#fff;margin-right:4px;vertical-align:-1px}
.like{background:#fff;color:var(--navy-deep);font-size:6.5px;padding:1px 4px;border-radius:2px}
.post{position:relative;background:#fff;height:70px;margin-bottom:5px;font-size:7.8px;line-height:12px;color:#444;padding:6px 6px 0 38px}
.community .post{height:64px}
.avatar{position:absolute;left:6px;top:7px;width:24px;height:22px;background:linear-gradient(#e9c6a8,#c99a7b)}
.post b{font-family:'Lato',sans-serif;font-weight:700;font-size:8px;color:#222}
.post .meta{color:#999;font-size:7px}
.post .date{position:absolute;right:6px;top:7px;color:#999;font-size:7px}
.post p{margin-left:-32px;margin-top:4px}

/* footer */
.site-footer{position:absolute;left:0;top:1120px;width:757px;height:80px;background:var(--footer);color:#fff}
.site-footer h3{position:absolute;top:12px;font-family:'Ubuntu',sans-serif;font-weight:500;font-size:12px}
.field{position:absolute;top:31px;height:16px;background:#fff;border-radius:2px;font-size:7.5px;font-style:italic;color:#666;padding:2px 5px}
.contact{position:absolute;font-size:7.6px;line-height:11.5px;font-weight:400}
.divider{position:absolute;top:12px;width:1px;height:58px;background:rgba(255,255,255,.35)}
.foot-brand{position:absolute;left:590px;top:14px;font-family:'Ubuntu',sans-serif;font-weight:700;font-size:17px;color:#9fd5a8}
.copy{position:absolute;left:578px;top:44px;width:92px;text-align:center;font-size:6.6px;line-height:9.5px}
</style>
</head>
<body>

<header class="site-header">
  <div class="brand"><span>PlayNest</span><span class="brand-dot"></span></div>
  <a class="top-link" style="left:478px;top:42px;--h:42px">New User?</a>
  <a class="top-link" style="left:535px;top:35px;--h:35px">Register</a>
  <a class="top-link" style="left:588px;top:30px;--h:30px">Login</a>
  <a class="top-link" style="left:631px;top:42px;--h:42px">&nbsp;&nbsp;Help&nbsp;&nbsp;</a>
  <nav class="main-nav">
    <div class="tab active">Home</div>
    <div class="tab">About Us</div>
    <div class="tab">Teachers</div>
    <div class="tab">Activities</div>
    <div class="tab">Career</div>
    <div class="tab">News &amp; Event</div>
    <div class="tab">Contact Us</div>
  </nav>
</header>

<section class="hero" role="img" aria-label="Photo of three smiling toddlers playing together in a bright playroom">
  <div class="hero-caption">The <b>PlayNest</b> Provide High Quality<br>of Care and Traning</div>
  <svg class="slider-corner" width="135" height="74" viewBox="0 0 135 74"><polygon points="135,0 135,74 0,74" fill="#3b3b98"/></svg>
  <div class="slider-dots"><span>1</span>2345</div>
</section>

<h1 class="welcome-title">Welcome</h1>
<div class="welcome-brand">PlayNest</div>
<p class="welcome-text">Lorem ipsum dolor sit amet, consectetuer adipiscing elit, sed diam nonummy nibh euismod tincidunt ut laoreet dolore magna aliquam erat volutpat. Ut wisi enim ad minim veniam, quis nostrud exerci tation ullamcorper suscipit lobortis nisl ut aliquip ex ea commodo consequat. Duis autem vel eum iriure dolor in hendrerit in vulputate velit esse molestie consequat, vel illum dolore eu feugiat nulla facilisis at vero eros et accumsan et iusto odio dignissim qui blandit praesent luptatum zzril delenit augue duis dolore te feugait nulla facilisis.</p>
<div class="btn btn-green" style="left:351px;top:603px;width:65px;height:20px;line-height:18px">Read More »</div>

<section class="features">
  <svg class="abs" style="left:0;top:0" width="757" height="255" viewBox="0 0 757 255"><path d="M0 10 Q180 30 380 20 T757 22 V255 H0 Z" fill="#efefef"/></svg>
  <article class="card" style="left:83px">
    <h2>Activities We Do</h2>
    <div class="photo" role="img" aria-label="Photo of a girl drawing at a classroom table" style="background:linear-gradient(120deg,#e4c6a6,#f0d64a)"></div>
    <p>Duis autem vel eum iriure dolor in hendre in vulputate velit ess molestie consequat, vel illum dolore facilisis.</p>
    <div class="btn btn-navy">Read More »</div>
  </article>
  <article class="card" style="left:287px">
    <h2>Our Teacher</h2>
    <div class="photo" role="img" aria-label="Photo of a smiling teacher with pupils in a classroom" style="background:linear-gradient(120deg,#ddd,#b8423a 50%,#d8a838)"></div>
    <p>Duis autem vel eum iriure dolor in hendre in vulputate velit ess molestie consequat, vel illum dolore facilisis.</p>
    <div class="btn btn-navy">Read More »</div>
  </article>
  <article class="card" style="left:491px">
    <h2>Up Coming Events</h2>
    <div class="photo" role="img" aria-label="Photo of children in costumes on a stage with red curtains" style="background:linear-gradient(120deg,#a3121a,#c83a2a 50%,#7aa52e)"></div>
    <p>Duis autem vel eum iriure dolor in hendre in vulputate velit ess molestie consequat, vel illum dolore facilisis.</p>
    <div class="btn btn-navy">Read More »</div>
  </article>
</section>

<h2 class="section-title" style="left:90px">See Us in Photos</h2>
<div class="insta" role="img" aria-label="Children running in autumn leaves" style="left:94px;top:946px;background:linear-gradient(#9cbf6a,#a8773e)"></div>
<div class="insta" role="img" aria-label="Children at a classroom table with a teacher" style="left:185px;top:946px;background:linear-gradient(#efe1c9,#d86a4e)"></div>
<div class="insta" role="img" aria-label="Girl with painted hands" style="left:277px;top:946px;background:linear-gradient(#f3eee8,#e5b986)"></div>
<div class="insta" role="img" aria-label="Group of children in a classroom" style="left:94px;top:1029px;background:linear-gradient(#7fb0d8,#d89a84)"></div>
<div class="insta" role="img" aria-label="Children jumping with arms raised" style="left:185px;top:1029px;background:linear-gradient(#e26a4a,#f0c24a)"></div>
<div class="insta" role="img" aria-label="Teacher painting with children" style="left:277px;top:1029px;background:linear-gradient(#eef0ee,#b2a58d)"></div>

<h2 class="section-title" style="left:379px">Latest Updates</h2>
<div class="feed updates">
  <div class="post"><div class="avatar" role="img" aria-label="Profile photo"></div><b>Lorem ipsum</b><span class="date">June 19</span><br><span class="meta">@PlayNest</span><p>Duis autem vel eum iriure in hendre in vulputate velit ess</p></div>
  <div class="post"><div class="avatar" role="img" aria-label="Profile photo"></div><b>Lorem ipsum</b><span class="date">June 19</span><br><span class="meta">@PlayNest</span><p>Duis autem vel eum iriure in hendre in vulputate velit ess</p></div>
</div>

<h2 class="section-title" style="left:532px">Community Posts</h2>
<div class="feed community">
  <div class="feed-head"><span><span class="dot"></span>PlayNest</span><span class="like">Like</span></div>
  <div class="post"><div class="avatar" role="img" aria-label="Profile photo"></div><b>Lorem ipsum</b><br><span class="meta">Posted on june 19</span><p>Duis autem vel eum iriure in hendre in vulputate velit ess</p></div>
  <div class="post"><div class="avatar" role="img" aria-label="Profile photo"></div><b>Lorem ipsum</b><br><span class="meta">Posted on june 19</span><p>Duis autem vel eum iriure in hendre in vulputate velit ess</p></div>
</div>

<footer class="site-footer">
  <h3 style="left:90px">Join The Mailing List</h3>
  <div class="field" style="left:90px;width:95px">Name</div>
  <div class="field" style="left:191px;width:95px">Email</div>
  <div class="btn btn-green" style="left:90px;top:56px;width:60px;height:16px;line-height:14px">Submit</div>

  <div class="divider" style="left:300px"></div>
  <h3 style="left:315px">Contact Information</h3>
  <svg class="abs" style="left:315px;top:33px" width="9" height="13" viewBox="0 0 9 13"><path d="M4.5 0A4.5 4.5 0 0 0 0 4.5C0 8 4.5 13 4.5 13S9 8 9 4.5A4.5 4.5 0 0 0 4.5 0Zm0 6.3a1.8 1.8 0 1 1 0-3.6 1.8 1.8 0 0 1 0 3.6Z" fill="#fff"/></svg>
  <div class="contact" style="left:333px;top:32px;width:115px">Lorem ipsum dolor sit ame consectetuer ina adipiscing consectetuer ina</div>
  <svg class="abs" style="left:453px;top:33px" width="9" height="9" viewBox="0 0 24 24"><path d="M6.6 10.8a15 15 0 0 0 6.6 6.6l2.2-2.2c.3-.3.7-.4 1-.2 1.1.4 2.3.6 3.6.6.6 0 1 .4 1 1V20c0 .6-.4 1-1 1A17 17 0 0 1 3 4c0-.6.4-1 1-1h3.5c.6 0 1 .4 1 1 0 1.3.2 2.5.6 3.6.1.3 0 .7-.2 1Z" fill="#fff"/></svg>
  <div class="contact" style="left:470px;top:32px;font-weight:700">01-234-567-890</div>
  <svg class="abs" style="left:453px;top:52px" width="9" height="7" viewBox="0 0 9 7"><rect width="9" height="7" fill="#fff"/><path d="M0 0 4.5 4 9 0" fill="none" stroke="#21a24a" stroke-width="1"/></svg>
  <div class="contact" style="left:470px;top:50px">hello@playnest.example</div>

  <div class="divider" style="left:574px"></div>
  <div class="foot-brand">PlayNest</div>
  <div class="copy">© Copyright © 2014 playnest.<br>All Rights Reserved.</div>
</footer>

</body>
</html>
```